Package design for small honey and vegetable farm

I would like to have a unique design for the packaging of our honey and vegetables. I have attached the logo from our farm "Willow Creek Acres" that should be on the packaging for both the honey and the vegetables

For the honey the writing, "100% pure organic honey" must be on the packaging in some place. As well as "from the busy bees at Willow Creek Acres". I have attached some designs that I like.

For the vegetables. The design will need to go on a box like the one in the attached image. The phrase "Organically Grown" should be on the package. I would like the background color of the package to be black. I think I would also like to see some stylized vegetables (tomatoes in particular) on the package.

I would like to be able to get all the colors (RGB) used in the designs so I can pass them on to printers.

Industry/Entity Type

Farm

Colors
fbee3e

Requirements
Must have
• For the honey, the package it must say "100% pure organic honey".
• For the vegetables I would like the background color to be black. I would also like some stylized vegetables (tomatoes in particular) added to the package.

```html
<!DOCTYPE html>
<html lang="en">
<head>
<meta charset="utf-8">
<title>Willow Creek Acres – Packaging</title>
<link href="https://fonts.googleapis.com/css2?family=Josefin+Sans:wght@400;600&family=Playfair+Display:wght@700&display=swap" rel="stylesheet">
<style>
  :root{
    --canvas:#ffffff;
    --box-black:#141414;
    --farm-yellow:#fbee3e;
    --label-gold:#f2d23a;
    --ribbon-lime:#d9d43c;
    --honey-orange:#f6ad25;
    --honey-light:#ffd84a;
    --honey-ink:#c4631c;
    --label-dark:#1f1f1d;
  }
  *{margin:0;padding:0;box-sizing:border-box}
  html,body{width:1200px;height:1080px;overflow:hidden;background:var(--canvas)}
  .artboard{position:relative;width:1200px;height:1080px;background:var(--canvas)}

  /* vegetable box side panel */
  .veg-box-panel{
    position:absolute;left:290px;top:90px;width:620px;height:370px;
    background:var(--box-black);
  }
  .veg-illustration{position:absolute;border-radius:50%}
  .veg-illustration--tomato{left:40px;bottom:40px;width:150px;height:150px;
    background:radial-gradient(circle at 45% 45%,rgba(251,238,62,.55),rgba(251,238,62,.12) 70%)}
  .veg-illustration--broccoli{left:200px;bottom:30px;width:80px;height:80px;
    background:radial-gradient(circle,rgba(251,238,62,.4),rgba(251,238,62,.08) 70%)}
  .veg-illustration--pumpkin{right:40px;top:40px;width:120px;height:150px;
    background:radial-gradient(circle at 50% 50%,rgba(251,238,62,.5),rgba(251,238,62,.1) 70%)}
  .box-tagline{
    position:absolute;left:300px;top:120px;
    font-family:"Playfair Display",serif;font-weight:700;font-size:24px;
    color:var(--farm-yellow);
  }
  .box-farm-name{
    position:absolute;left:270px;top:170px;width:300px;text-align:center;
    font-family:"Josefin Sans",sans-serif;font-weight:400;font-size:40px;line-height:1.1;
    color:var(--farm-yellow);
  }

  /* honey labels */
  .honey-label{position:absolute;top:680px;width:300px;height:300px;overflow:visible}
  .honey-label--hex{left:215px}
  .honey-label--splash{left:705px}
  .label-text{font-family:"Josefin Sans",sans-serif;font-weight:400}
</style>
</head>
<body>
<main class="artboard">

  <section class="veg-box-panel" aria-label="Vegetable box side panel">
    <div class="veg-illustration veg-illustration--tomato" role="img" aria-label="Stylized line drawing of a sliced tomato"></div>
    <div class="veg-illustration veg-illustration--broccoli" role="img" aria-label="Stylized line drawing of broccoli"></div>
    <div class="veg-illustration veg-illustration--pumpkin" role="img" aria-label="Stylized line drawing of a pumpkin and potatoes"></div>
    <p class="box-tagline">Organically Grown</p>
    <p class="box-farm-name">Willow Creek Acres</p>
  </section>

  <svg class="honey-label honey-label--hex" viewBox="0 0 300 300" aria-label="Honey jar label, dark hexagon">
    <defs>
      <path id="hexArcTop" d="M72 195 A90 90 0 1 1 228 195"/>
      <path id="hexArcBottom" d="M58 150 A92 92 0 0 0 242 150"/>
    </defs>
    <polygon points="150,20 262,85 262,215 150,280 38,215 38,85" fill="var(--label-dark)"/>
    <polygon points="150,30 253,90 253,210 150,270 47,210 47,90" fill="none" stroke="var(--label-gold)" stroke-width="2"/>
    <polygon points="0,125 40,125 40,175 0,175 14,150" fill="var(--ribbon-lime)"/>
    <polygon points="300,125 260,125 260,175 300,175 286,150" fill="var(--ribbon-lime)"/>
    <rect x="30" y="130" width="240" height="40" fill="var(--ribbon-lime)"/>
    <text class="label-text" font-size="14" fill="var(--label-gold)" letter-spacing="1">
      <textPath href="#hexArcTop" startOffset="50%" text-anchor="middle">100% PURE ORGANIC HONEY</textPath>
    </text>
    <text class="label-text" x="150" y="158" font-size="22" text-anchor="middle" fill="var(--label-dark)">Willow Creek Acres</text>
    <text class="label-text" font-size="10" fill="var(--label-gold)">
      <textPath href="#hexArcBottom" startOffset="50%" text-anchor="middle">From the busy bees at Willow Creek Acres</textPath>
    </text>
  </svg>

  <svg class="honey-label honey-label--splash" viewBox="0 0 300 300" aria-label="Honey jar label, golden splash">
    <defs>
      <radialGradient id="splashFill" cx="50%" cy="45%" r="55%">
        <stop offset="0" stop-color="var(--honey-light)"/>
        <stop offset="1" stop-color="var(--honey-orange)"/>
      </radialGradient>
      <path id="splashArcTop" d="M72 195 A90 90 0 1 1 228 195"/>
      <path id="splashArcBottom" d="M62 150 A88 88 0 0 0 238 150"/>
    </defs>
    <circle cx="150" cy="150" r="118" fill="url(#splashFill)"/>
    <text class="label-text" font-size="14" fill="var(--honey-ink)" letter-spacing="1">
      <textPath href="#splashArcTop" startOffset="50%" text-anchor="middle">100% PURE ORGANIC HONEY</textPath>
    </text>
    <text class="label-text" x="150" y="158" font-size="22" text-anchor="middle" fill="var(--honey-ink)">Willow Creek Acres</text>
    <text class="label-text" font-size="10" fill="var(--honey-ink)">
      <textPath href="#splashArcBottom" startOffset="50%" text-anchor="middle">From the busy bees at Willow Creek Acres</textPath>
    </text>
  </svg>

</main>
</body>
</html>
```